Letterhead and Business Cards

Using our new logo we would like designs for the following,

1.Letterhead

2. 2 x Business Cards

I will need all three in high quality PDF files ready for printing. I will also require the top and bottom of the letterhead as two JPG files.

Target Market(s)

We are a business to business company dealing with middle to upper management both as clients and suppliers.

Industry/Entity Type

Business

Requirements
Must have
• 1. Look professional.
• 2. Utilise our logo colours
• 3. Incorporate our logo on both.
• 4. Letterhead

• Address:
• Pell Harrow Court
• Pell Harrow Lane
• London
• WC1R 4JZ

• Tel:0845 312 4096
• Fax: 0845 312 7158
• Website: www.kovimerlox.com
• Email: info@kovimerlox.com

• Directors: D.R. Marsh and H.J. Marsh Company Registration No: 52064918(This should be quite small in the letterhead footer somewhere)

• Business Card One Sided Only

• 1. Dominic R. Marsh
• Managing Director

• Address:
• Pell Harrow Court
• Pell Harrow Lane
• London
• WC1R 4JZ

• Tel:0845 312 4096
• Fax: 0845 312 7159
• Mob: 0791 526 3307
• Email: dominic@kovimerlox.com

• 2. Helen J. Marsh
• Sales Director

• Address:
• Pell Harrow Court
• Pell Harrow Lane
• London
• WC1R 4JZ

• Tel:0845 312 4096
• Fax: 0845 312 7158
• Mob: 0794 862 1190
• Email: helen@kovimerlox.com

• Please note some of this info may change for final printing.

```html
<!DOCTYPE html>
<html lang="en">
<head>
<meta charset="utf-8">
<title>Kovimerlox Stationery</title>
<link href="https://fonts.googleapis.com/css2?family=Arimo:wght@400;700&display=swap" rel="stylesheet">
<style>
  :root {
    --brand-green: #85bc00;
    --brand-grey: #9a9fa1;
    --ink: #161616;
    --frame: #3a3a3a;
    --paper: #ffffff;
  }
  * { margin: 0; padding: 0; box-sizing: border-box; }
  html, body { width: 979px; height: 1200px; overflow: hidden; background: var(--paper); }
  body { position: relative; font-family: "Arimo", Arial, sans-serif; color: var(--ink); }

  .letterhead {
    position: absolute; left: 130px; top: 0; width: 849px; height: 1199px;
    border: 1px solid var(--frame); border-right: none; background: var(--paper);
  }
  .lh-top-band { position: absolute; left: 651px; top: 0; width: 169px; height: 41px; background: var(--brand-green); }
  .lh-brand { position: absolute; left: 651px; top: 66px; width: 169px; text-align: center; }
  .lh-side-band {
    position: absolute; left: 651px; top: 194px; width: 169px; height: 630px;
    background: linear-gradient(to bottom, var(--brand-green) 0%, #b9d974 40%, #e8f2d2 75%, rgba(255,255,255,0) 100%);
  }
  .brand-dot { display: block; margin: 0 auto; border-radius: 50%; background: var(--brand-green); }
  .brand-name { display: block; font-weight: 700; color: var(--brand-grey); letter-spacing: -0.5px; }
  .lh-brand .brand-dot { width: 74px; height: 74px; }
  .lh-brand .brand-name { font-size: 25px; margin-top: 16px; }

  .lh-footer { position: absolute; left: 651px; top: 911px; width: 169px; font-size: 12px; line-height: 16px; white-space: nowrap; }
  .lh-footer .rule { height: 1px; background: var(--brand-green); margin: 10px 0 11px; }
  .lh-footer .label { font-weight: 700; }
  .lh-footer .reg { font-size: 8.5px; letter-spacing: 0.3px; line-height: 12px; }

  .card {
    position: absolute; width: 344px; height: 223px;
    border: 1px solid var(--frame); background: var(--paper); overflow: hidden;
  }
  .card-one { left: 0; top: 420px; }
  .card-two { left: 1px; top: 715px; }
  .card-panel { position: absolute; left: 0; top: 0; }
  .card-address, .card-contact { position: absolute; left: 15px; font-size: 11.2px; line-height: 15.4px; white-space: nowrap; }
  .card-address { top: 20px; }
  .card-contact { top: 128px; }
  .card-person { position: absolute; right: 16px; top: 21px; text-align: right; }
  .card-name { font-size: 13px; font-weight: 700; line-height: 16px; }
  .card-role { font-size: 9px; color: var(--brand-green); margin-top: 2px; }
  .card-brand { position: absolute; left: 205px; top: 124px; width: 128px; text-align: center; }
  .card-brand .brand-dot { width: 54px; height: 54px; }
  .card-brand .brand-name { font-size: 17px; margin-top: 9px; }
  .tab { display: inline-block; width: 27px; }
</style>
</head>
<body>

<section class="letterhead">
  <div class="lh-top-band"></div>
  <div class="lh-brand">
    <span class="brand-dot"></span>
    <span class="brand-name">Kovimerlox</span>
  </div>
  <div class="lh-side-band"></div>

  <footer class="lh-footer">
    <p>Pell Harrow Court<br>Pell Harrow Lane<br>London<br>WC1R 4JZ</p>
    <div class="rule"></div>
    <p>Tel&nbsp;&nbsp;&nbsp; : 0845 312 4096<br>Fax&nbsp; : 0845 312 7158<br>Email: info@kovimerlox.com<br>Website: www.kovimerlox.com</p>
    <div class="rule"></div>
    <p class="label">Directors:</p>
    <p>D.R. Marsh&nbsp; I&nbsp; H.J. Marsh</p>
    <div class="rule"></div>
    <p class="reg">Company Registration No: 52064918</p>
  </footer>
</section>

<article class="card card-one">
  <svg class="card-panel" width="344" height="223" viewBox="0 0 344 223" aria-hidden="true">
    <path d="M0 0 H210 C182 28 167 68 167 110 C167 154 186 194 221 223 H0 Z" fill="var(--brand-green)"/>
  </svg>
  <p class="card-address">Pell Harrow Court<br>Pell Harrow Lane<br>London<br>WC1R 4JZ</p>
  <p class="card-contact"><span class="tab">Tel</span>: 0845 312 4096<br><span class="tab">Fax</span>: 0845 312 7159<br><span class="tab">Mob</span>: 0791 526 3307<br>Email: dominic@kovimerlox.com<br>Website: www.kovimerlox.com</p>
  <div class="card-person">
    <p class="card-name">Dominic R. Marsh</p>
    <p class="card-role">Managing Director</p>
  </div>
  <div class="card-brand">
    <span class="brand-dot"></span>
    <span class="brand-name">Kovimerlox</span>
  </div>
</article>

<article class="card card-two">
  <svg class="card-panel" width="344" height="223" viewBox="0 0 344 223" aria-hidden="true">
    <path d="M0 0 H210 C182 28 167 68 167 110 C167 154 186 194 221 223 H0 Z" fill="var(--brand-green)"/>
  </svg>
  <p class="card-address">Pell Harrow Court<br>Pell Harrow Lane<br>London<br>WC1R 4JZ</p>
  <p class="card-contact"><span class="tab">Tel</span>: 0845 312 4096<br><span class="tab">Fax</span>: 0845 312 7158<br><span class="tab">Mob</span>: 0794 862 1190<br>Email: helen@kovimerlox.com<br>Website: www.kovimerlox.com</p>
  <div class="card-person">
    <p class="card-name">Helen J. Marsh</p>
    <p class="card-role">Sales Director</p>
  </div>
  <div class="card-brand">
    <span class="brand-dot"></span>
    <span class="brand-name">Kovimerlox</span>
  </div>
</article>

</body>
</html>
```